Business Card Design Project - Industrial Motor Rep

Create a business card that utilizes our existing logo found on our website: www.kestrelfluxsupply.com

We are a Industrial Distributor with a focus on electric motors. We represent several key brands which can be found on our web site. Our customer base includes Consultants, Large End Users (TQ, Lusk Chemical, Brevol) and original equipment manufacturers.

Industry/Entity Type

Business

Requirements
Must have
• Name, Title, Phone, Fax, Cell, Website, Mailing address

```html
<!DOCTYPE html>
<html lang="en">
<head>
<meta charset="UTF-8">
<title>Kestrel Flux Supply – Business Card</title>
<link href="https://fonts.googleapis.com/css2?family=Open+Sans:wght@400;600;700&display=swap" rel="stylesheet">
<style>
  :root {
    --page-bg: #ffffff;
    --card-bg: #000000;
    --brand-grey: #a9a9ab;
    --tagline-grey: #8e8e90;
    --brand-blue: #1f66b0;
    --brand-red: #e8233f;
    --text-white: #ffffff;
    --divider: #6a6a6a;
  }
  * { margin: 0; padding: 0; box-sizing: border-box; }
  html, body {
    width: 1200px; height: 900px; overflow: hidden;
    background: var(--page-bg);
    font-family: "Open Sans", Arial, sans-serif;
  }
  .canvas { position: relative; width: 1200px; height: 900px; }

  .card {
    position: absolute;
    width: 600px; height: 340px;
    background: var(--card-bg);
    border-radius: 30px;
    overflow: hidden;
  }
  .card--front { left: 110px; top: 70px; }
  .card--back  { left: 500px; top: 480px; }

  /* Brand lockup */
  .brand { position: absolute; display: flex; flex-direction: column; align-items: center; }
  .brand__mark {
    border-radius: 50%;
    border: 6px solid var(--brand-blue);
  }
  .brand__name {
    color: var(--brand-grey);
    font-weight: 700;
    white-space: nowrap;
    letter-spacing: 0.5px;
  }
  .brand__tagline {
    color: var(--tagline-grey);
    font-weight: 400;
    white-space: nowrap;
  }

  .card--front .brand { left: 0; right: 0; top: 58px; }
  .card--front .brand__mark { width: 120px; height: 120px; margin-bottom: 20px; }
  .card--front .brand__name { font-size: 34px; line-height: 1.1; }
  .card--front .brand__tagline { font-size: 21px; margin-top: 2px; }

  .card--back .brand { left: 18px; width: 272px; top: 96px; }
  .card--back .brand__mark { width: 72px; height: 72px; border-width: 4px; margin-bottom: 12px; }
  .card--back .brand__name { font-size: 18px; line-height: 1.1; }
  .card--back .brand__tagline { font-size: 12px; margin-top: 1px; }

  .divider {
    position: absolute; left: 300px; top: 110px;
    width: 1px; height: 200px; background: var(--divider);
  }

  .contact { position: absolute; left: 322px; top: 112px; color: var(--text-white); }
  .contact__name { font-size: 28px; font-weight: 600; line-height: 1.1; }
  .contact__title { font-size: 17px; font-weight: 700; margin-bottom: 40px; }
  .contact__list { list-style: none; }
  .contact__item {
    display: flex; align-items: center;
    font-size: 15px; line-height: 22px; height: 22px;
  }
  .contact__icon { width: 16px; height: 16px; margin-right: 10px; flex: none; }
  .contact__icon * { fill: var(--brand-blue); }
</style>
</head>
<body>
<main class="canvas">

  <section class="card card--front" aria-label="Business card front">
    <div class="brand">
      <div class="brand__mark"></div>
      <div class="brand__name">KESTREL FLUX SUPPLY, LLC</div>
      <div class="brand__tagline">Manufacturers Representatives</div>
    </div>
  </section>

  <section class="card card--back" aria-label="Business card back">
    <div class="brand">
      <div class="brand__mark"></div>
      <div class="brand__name">KESTREL FLUX SUPPLY, LLC</div>
      <div class="brand__tagline">Manufacturers Representatives</div>
    </div>

    <div class="divider"></div>

    <div class="contact">
      <div class="contact__name">Dale Hartwick</div>
      <div class="contact__title">Director</div>
      <ul class="contact__list">
        <li class="contact__item">
          <svg class="contact__icon" viewBox="0 0 16 16" aria-label="Phone"><path d="M1 5c0-2 2-3 7-3s7 1 7 3v1h-4V5H5v1H1zM3 7h10l1 7H2z"/></svg>
          555-301-4826
        </li>
        <li class="contact__item">
          <svg class="contact__icon" viewBox="0 0 16 16" aria-label="Fax"><path d="M4 1h7v4H4zM1 6h14v8H1zM4 9h8v1H4z"/></svg>
          555-019-2273
        </li>
        <li class="contact__item">
          <svg class="contact__icon" viewBox="0 0 16 16" aria-label="Mobile"><path d="M4 0h8a1 1 0 0 1 1 1v14a1 1 0 0 1-1 1H4a1 1 0 0 1-1-1V1a1 1 0 0 1 1-1zm1 2v10h6V2z"/></svg>
          xxx-xxx-xxxx
        </li>
        <li class="contact__item">
          <svg class="contact__icon" viewBox="0 0 16 16" aria-label="Website"><path d="M8 1a7 7 0 1 0 0 14A7 7 0 0 0 8 1zm0 1.5c.8 0 1.8 1.9 2 4.7H6c.2-2.8 1.2-4.7 2-4.7zM2.6 7.2A5.5 5.5 0 0 1 5.4 3 9 9 0 0 0 4.5 7.2zm0 1.6h1.9A9 9 0 0 0 5.4 13a5.5 5.5 0 0 1-2.8-4.2zM6 8.8h4c-.2 2.8-1.2 4.7-2 4.7s-1.8-1.9-2-4.7zm5.5 0h1.9a5.5 5.5 0 0 1-2.8 4.2 9 9 0 0 0 .9-4.2zm0-1.6a9 9 0 0 0-.9-4.2 5.5 5.5 0 0 1 2.8 4.2z"/></svg>
          www.kestrelfluxsupply.com
        </li>
        <li class="contact__item">
          <svg class="contact__icon" viewBox="0 0 16 16" aria-label="Email"><path d="M1 3h14v1L8 9 1 4zm0 2.5 7 5 7-5V13H1z"/></svg>
          dale@kestrelfluxsupply.com
        </li>
      </ul>
    </div>
  </section>

</main>
</body>
</html>
```